Re-drawing and gpahically, according to coorporate design

Three flowcharts need to be re-drawn and graphically improved according to coorporate design

```html
<!DOCTYPE html>
<html lang="en">
<head>
<meta charset="utf-8">
<title>CO₂ and biomass value chains</title>
<link rel="stylesheet" href="https://fonts.googleapis.com/css2?family=Quicksand:wght@500;600;700&display=swap">
<style>
  :root{
    --teal:#456466;
    --lime:#c6d85a;
    --olive:#a3a514;
    --frame:#c8cbcc;
    --paper:#ffffff;
    --backdrop:#e8ebed;
    --grey:#6f7b7d;
  }
  html,body{margin:0;padding:0;width:1200px;height:923px;overflow:hidden;background:var(--backdrop);}
  .poster{position:absolute;left:252px;top:0;width:696px;height:923px;background:var(--paper);}
  .poster svg{display:block;width:100%;height:100%;font-family:"Quicksand",sans-serif;}
  .lbl{font-weight:700;font-size:11px;letter-spacing:.3px;}
  .lbl-dark{fill:var(--teal);}
  .lbl-light{fill:#fff;}
  .lbl-box{fill:var(--teal);font-size:11px;font-weight:700;}
  .node-dark{fill:var(--teal);stroke:var(--frame);stroke-width:2;}
  .node-outline{fill:#fff;stroke:var(--teal);stroke-width:2.5;}
  .node-lime{fill:#fff;stroke:var(--lime);stroke-width:2.5;}
  .box-dark{fill:var(--teal);stroke:var(--frame);stroke-width:2;}
  .box-lime{fill:var(--lime);stroke:var(--teal);stroke-width:2;}
  .frame{fill:#fff;stroke:var(--frame);stroke-width:2;}
  .flow{stroke:var(--teal);stroke-width:3;fill:none;}
  .flow-olive{stroke:var(--olive);stroke-width:3;fill:none;}
  .flow-lime{stroke:var(--lime);stroke-width:3;fill:none;}
  .partner{font-weight:700;font-size:11px;fill:var(--teal);}
  .partner-sm{font-weight:700;font-size:8px;fill:var(--teal);}
  .brand{font-weight:700;font-size:22px;fill:var(--olive);}
  .brand-sub{font-weight:600;font-size:10px;fill:var(--teal);}
  .uni{font-weight:700;font-size:13px;fill:var(--grey);letter-spacing:1px;}
</style>
</head>
<body>
<div class="poster">
<svg viewBox="318 58 666 884" xmlns="http://www.w3.org/2000/svg" aria-label="Value chains from sunlight and CO₂ to products">
  <defs>
    <marker id="ah" viewBox="0 0 10 10" refX="7" refY="5" markerWidth="4" markerHeight="4" orient="auto"><path d="M0,0 L10,5 L0,10 z" fill="#456466"/></marker>
    <marker id="ah-olive" viewBox="0 0 10 10" refX="7" refY="5" markerWidth="4" markerHeight="4" orient="auto"><path d="M0,0 L10,5 L0,10 z" fill="#a3a514"/></marker>
    <marker id="ah-lime" viewBox="0 0 10 10" refX="7" refY="5" markerWidth="4" markerHeight="4" orient="auto"><path d="M0,0 L10,5 L0,10 z" fill="#c6d85a"/></marker>
  </defs>

  <!-- header -->
  <g class="header">
    <circle cx="355" cy="94" r="12" fill="none" stroke="var(--grey)" stroke-width="2"/>
    <text class="brand" x="372" y="98">ENERGYWORKS</text>
    <text class="brand-sub" x="372" y="110">Institute at Veldana University</text>
    <text class="uni" x="960" y="98" text-anchor="end">VELDANA</text>
    <line x1="318" y1="117" x2="984" y2="117" stroke="var(--olive)" stroke-width="1"/>
  </g>

  <!-- sun -->
  <g class="sun" fill="var(--lime)" stroke="var(--teal)" stroke-width="1.5">
    <circle cx="363" cy="195" r="26"/>
    <path d="M363,150 l6,10 h-12z M363,240 l6,-10 h-12z M318,195 l10,6 v-12z M408,195 l-10,6 v-12z M331,163 l11,3 -8,8z M395,163 l-11,3 8,8z M331,227 l11,-3 -8,-8z M395,227 l-11,-3 8,-8z"/>
  </g>

  <!-- top chain -->
  <line class="flow" x1="411" y1="195" x2="493" y2="195" marker-end="url(#ah)"/>
  <circle class="node-outline" cx="532" cy="195" r="32"/>
  <g fill="none" stroke="var(--teal)" stroke-width="1.8">
    <path d="M518,206 l8,-20 8,20z M530,206 l8,-20 8,20z M524,210 l8,-20 8,20z"/>
    <path d="M526,206v6 M538,206v6 M532,210v6"/>
  </g>
  <text class="lbl lbl-dark" x="532" y="240" text-anchor="middle">agriculture/</text>
  <text class="lbl lbl-dark" x="532" y="253" text-anchor="middle">forestry</text>
  <line class="flow" x1="565" y1="195" x2="603" y2="195" marker-end="url(#ah)"/>
  <circle class="node-outline" cx="640" cy="195" r="32"/>
  <text class="lbl lbl-dark" x="640" y="199" text-anchor="middle">industry</text>
  <line class="flow" x1="673" y1="193" x2="815" y2="157" marker-end="url(#ah)"/>
  <line class="flow" x1="673" y1="197" x2="815" y2="235" marker-end="url(#ah)"/>
  <circle class="node-outline" cx="852" cy="161" r="32"/>
  <text class="lbl lbl-dark" x="852" y="160" text-anchor="middle">food/</text>
  <text class="lbl lbl-dark" x="852" y="171" text-anchor="middle">feed</text>
  <circle class="node-outline" cx="852" cy="230" r="32"/>
  <text class="lbl lbl-dark" x="852" y="222" text-anchor="middle">wood</text>
  <text class="lbl lbl-dark" x="852" y="233" text-anchor="middle">based</text>
  <text class="lbl lbl-dark" x="852" y="244" text-anchor="middle">products</text>

  <!-- residues -->
  <line class="flow" x1="640" y1="228" x2="640" y2="262" marker-end="url(#ah)"/>
  <path class="flow" d="M532,258 V298 H604" marker-end="url(#ah)"/>
  <circle class="node-dark" cx="641" cy="298" r="31"/>
  <text class="lbl lbl-light" x="641" y="302" text-anchor="middle">residues</text>
  <line class="flow" x1="620" y1="334" x2="584" y2="361" marker-end="url(#ah)"/>
  <line class="flow" x1="641" y1="330" x2="641" y2="361" marker-end="url(#ah)"/>
  <line class="flow" x1="662" y1="334" x2="698" y2="361" marker-end="url(#ah)"/>

  <!-- conversion boxes -->
  <rect class="box-dark" x="510" y="367" width="85" height="57" rx="5"/>
  <text class="lbl lbl-light" x="552" y="391" text-anchor="middle">anaerobic</text>
  <text class="lbl lbl-light" x="552" y="405" text-anchor="middle">digestion</text>
  <rect class="box-dark" x="599" y="367" width="85" height="57" rx="5"/>
  <text class="lbl lbl-light" x="641" y="391" text-anchor="middle">biomass</text>
  <text class="lbl lbl-light" x="641" y="405" text-anchor="middle">gasification</text>
  <rect class="box-dark" x="688" y="367" width="85" height="57" rx="5"/>
  <text class="lbl lbl-light" x="730" y="399" text-anchor="middle">fermentation</text>

  <!-- CO4 -->
  <line class="flow-olive" x1="509" y1="394" x2="494" y2="394" marker-end="url(#ah-olive)"/>
  <circle class="node-lime" cx="463" cy="393" r="25" style="stroke:var(--olive)"/>
  <text x="459" y="400" text-anchor="middle" font-weight="600" font-size="19" fill="var(--olive)">CO<tspan font-size="9" dy="4">4</tspan></text>
  <rect x="416" y="418" width="94" height="27" fill="#f3f4f4"/>
  <text class="partner-sm" x="463" y="434" text-anchor="middle">Tessary</text>

  <!-- right products -->
  <line class="flow" x1="774" y1="394" x2="815" y2="340" marker-end="url(#ah)"/>
  <line class="flow" x1="774" y1="396" x2="815" y2="396" marker-end="url(#ah)"/>
  <line class="flow" x1="774" y1="398" x2="815" y2="450" marker-end="url(#ah)"/>
  <rect class="frame" x="824" y="295" width="152" height="63" rx="9"/>
  <rect class="frame" x="824" y="363" width="152" height="64" rx="9"/>
  <rect class="frame" x="824" y="432" width="152" height="63" rx="9"/>
  <circle class="node-dark" cx="852" cy="326" r="31"/>
  <text class="lbl lbl-light" x="852" y="330" text-anchor="middle">polymers</text>
  <circle class="node-dark" cx="852" cy="395" r="31"/>
  <text class="lbl lbl-light" x="852" y="399" text-anchor="middle">chemicals</text>
  <circle class="node-dark" cx="852" cy="463" r="31"/>
  <text class="lbl lbl-light" x="852" y="467" text-anchor="middle">fuel</text>
  <text class="partner" x="930" y="330" text-anchor="middle">Quillon</text>
  <text class="partner" x="930" y="388" text-anchor="middle">Brenko</text>
  <text class="partner" x="930" y="419" text-anchor="middle">Talvex</text>
  <text class="partner" x="930" y="454" text-anchor="middle">Norbin</text>
  <text class="partner" x="930" y="484" text-anchor="middle">Pelvara</text>

  <!-- to CO2 -->
  <line class="flow" x1="568" y1="425" x2="626" y2="455" marker-end="url(#ah)"/>
  <line class="flow" x1="641" y1="425" x2="641" y2="455" marker-end="url(#ah)"/>
  <line class="flow" x1="714" y1="425" x2="656" y2="455" marker-end="url(#ah)"/>
  <circle class="node-lime" cx="640" cy="487" r="25" style="stroke:var(--olive)"/>
  <text x="637" y="494" text-anchor="middle" font-weight="600" font-size="19" fill="var(--olive)">CO<tspan font-size="9" dy="-8">2</tspan></text>

  <!-- left column -->
  <line class="flow" x1="363" y1="246" x2="363" y2="292" marker-end="url(#ah)"/>
  <circle class="node-dark" cx="363" cy="331" r="32"/>
  <circle cx="363" cy="331" r="17" fill="none" stroke="#fff" stroke-width="2"/>
  <path d="M366,318 l-9,14 h7 l-4,12 10,-15 h-7z" fill="#fff"/>
  <text class="lbl lbl-dark" x="363" y="374" text-anchor="middle">renewable</text>
  <text class="lbl lbl-dark" x="363" y="387" text-anchor="middle">electricity</text>
  <line class="flow" x1="363" y1="392" x2="363" y2="430" marker-end="url(#ah)"/>
  <circle class="node-dark" cx="363" cy="468" r="32"/>
  <g fill="none" stroke="#fff" stroke-width="1.8">
    <rect x="349" y="458" width="28" height="24" rx="2"/>
    <path d="M356,452v18 M370,452v18 M352,452h8 M366,452h8"/>
  </g>
  <text class="lbl lbl-dark" x="363" y="511" text-anchor="middle">electrolysis</text>
  <line class="flow" x1="363" y1="516" x2="363" y2="554" marker-end="url(#ah)"/>
  <circle class="node-dark" cx="363" cy="592" r="32"/>
  <text x="360" y="598" text-anchor="middle" font-weight="700" font-size="16" fill="#fff">H<tspan font-size="9" dy="4">2</tspan></text>
  <line class="flow" x1="396" y1="592" x2="416" y2="592" marker-end="url(#ah)"/>
  <line class="flow" x1="363" y1="645" x2="363" y2="684" marker-end="url(#ah)"/>
  <rect class="box-dark" x="323" y="690" width="80" height="55" rx="3"/>
  <text class="lbl lbl-light" x="337" y="710" font-size="10">▪ mobility</text>
  <text class="lbl lbl-light" x="337" y="722" font-size="10">▪ industry</text>
  <text class="lbl lbl-light" x="337" y="734" font-size="10">▪ gas grid</text>
  <text class="lbl lbl-dark" x="363" y="759" text-anchor="middle">various direct</text>
  <text class="lbl lbl-dark" x="363" y="773" text-anchor="middle">applications</text>

  <!-- CO2 pathways -->
  <line class="flow-olive" x1="628" y1="513" x2="488" y2="545" marker-end="url(#ah-olive)"/>
  <line class="flow-olive" x1="634" y1="513" x2="556" y2="545" marker-end="url(#ah-olive)"/>
  <line class="flow-olive" x1="641" y1="513" x2="641" y2="545" marker-end="url(#ah-olive)"/>
  <line class="flow-olive" x1="648" y1="513" x2="698" y2="545" marker-end="url(#ah-olive)"/>
  <line class="flow-olive" x1="654" y1="513" x2="796" y2="545" marker-end="url(#ah-olive)"/>

  <rect class="box-lime" x="421" y="555" width="85" height="57" rx="5"/>
  <text class="lbl-box" x="463" y="573" text-anchor="middle">catalytic/</text>
  <text class="lbl-box" x="463" y="587" text-anchor="middle">biological</text>
  <text class="lbl-box" x="463" y="601" text-anchor="middle">methanation</text>
  <rect class="box-lime" x="510" y="555" width="85" height="57" rx="5"/>
  <text class="lbl-box" x="552" y="573" text-anchor="middle">electro-</text>
  <text class="lbl-box" x="552" y="587" text-anchor="middle">chemical</text>
  <text class="lbl-box" x="552" y="601" text-anchor="middle">conversion</text>
  <rect class="box-lime" x="599" y="555" width="85" height="57" rx="5"/>
  <text class="lbl-box" x="641" y="573" text-anchor="middle">other</text>
  <text class="lbl-box" x="641" y="587" text-anchor="middle">chemical</text>
  <text class="lbl-box" x="641" y="600" text-anchor="middle" font-size="9">transformations</text>
  <rect class="box-lime" x="688" y="555" width="85" height="57" rx="5"/>
  <text class="lbl-box" x="730" y="572" text-anchor="middle">existing</text>
  <text class="lbl-box" x="730" y="586" text-anchor="middle">industrial</text>
  <text class="lbl-box" x="730" y="600" text-anchor="middle">applications</text>
  <rect class="box-lime" x="777" y="555" width="84" height="57" rx="5"/>
  <text class="lbl-box" x="819" y="587" text-anchor="middle">algea</text>

  <!-- outputs -->
  <line class="flow-lime" x1="463" y1="613" x2="463" y2="680" marker-end="url(#ah-lime)"/>
  <line class="flow-lime" x1="552" y1="613" x2="552" y2="680" marker-end="url(#ah-lime)"/>
  <line class="flow-lime" x1="641" y1="613" x2="641" y2="680" marker-end="url(#ah-lime)"/>
  <line class="flow-lime" x1="730" y1="613" x2="730" y2="680" marker-end="url(#ah-lime)"/>
  <line class="flow-lime" x1="819" y1="613" x2="819" y2="680" marker-end="url(#ah-lime)"/>

  <rect class="frame" x="431" y="700" width="65" height="147" rx="8"/>
  <rect class="frame" x="520" y="700" width="65" height="87" rx="8"/>
  <circle class="node-lime" cx="463" cy="718" r="32"/>
  <text x="460" y="724" text-anchor="middle" font-weight="600" font-size="17" fill="var(--teal)">CH<tspan font-size="9" dy="4">4</tspan></text>
  <circle class="node-lime" cx="552" cy="718" r="32"/>
  <text class="lbl-box" x="552" y="708" text-anchor="middle">e.g.</text>
  <text x="552" y="719" text-anchor="middle" font-weight="600" font-size="7" fill="var(--teal)">ethylene-oxide</text>
  <text x="552" y="735" text-anchor="middle" font-weight="600" font-size="15" fill="var(--teal)">C<tspan font-size="8" dy="3">2</tspan><tspan dy="-3">H</tspan><tspan font-size="8" dy="3">4</tspan><tspan dy="-3">O</tspan></text>
  <circle class="node-lime" cx="641" cy="718" r="32"/>
  <text class="lbl-box" x="641" y="706" text-anchor="middle" font-size="10">e.g.</text>
  <text class="lbl-box" x="641" y="717" text-anchor="middle" font-size="10">polyols,</text>
  <text class="lbl-box" x="641" y="728" text-anchor="middle" font-size="10">polymers,</text>
  <text class="lbl-box" x="641" y="739" text-anchor="middle" font-size="10">etc...</text>
  <circle class="node-lime" cx="730" cy="718" r="32"/>
  <text class="lbl-box" x="730" y="710" text-anchor="middle" font-size="10">e.g.</text>
  <text class="lbl-box" x="730" y="721" text-anchor="middle" font-size="10">beverage</text>
  <text class="lbl-box" x="730" y="732" text-anchor="middle" font-size="10">industry</text>
  <circle class="node-lime" cx="819" cy="718" r="32"/>
  <text class="lbl-box" x="819" y="710" text-anchor="middle" font-size="10">fuel,</text>
  <text class="lbl-box" x="819" y="721" text-anchor="middle" font-size="10">bio-</text>
  <text class="lbl-box" x="819" y="732" text-anchor="middle" font-size="10">polymers</text>

  <!-- partner names -->
  <text class="partner-sm" x="463" y="767" text-anchor="middle">Ombris</text>
  <text class="partner-sm" x="463" y="787" text-anchor="middle">Cresto</text>
  <text class="partner-sm" x="463" y="811" text-anchor="middle">Dravik</text>
  <text class="partner-sm" x="463" y="831" text-anchor="middle">Varnel</text>
  <text class="partner-sm" x="552" y="771" text-anchor="middle">Lumora</text>
  <text class="partner-sm" x="740" y="656">Dravik</text>

  <!-- footer band -->
  <rect x="318" y="887" width="666" height="23" fill="var(--olive)"/>
</svg>
</div>
</body>
</html>
```